Stakeline Manufacturing Company Needs a Website Design

We manufacture a variety of products including yard signs and would like to develop a stand alone website to cater to this business unit.

Competitor sites:
https://www.plakrova.com/yard-signs/
http://www.tavlune.com/

A few things to keep in mind/ elements we like from the competitors sites:
1) We do offer design services if someone dones not have a design

2) We would like the user to have the option to either select a template (based on industry: political, real estate, etc) or upload their own file

3) the site will focus on yard signs exclusively

4) Pricing, turn times, and ease of use seem to be the biggest factors in selecting a manufacturer

5) User experience/ flow is very important to us. We would like someone to be able to move forward with their sign selection/creation within the first click.

I like the "post a project" feel of mokrastudio.
Also, brelvato.com does a nice job of making it easy for the user to complete project with just a few clicks.

Pages I would like designed are the #1) homepage (prefer user to select whether to upload their own design or a template) #2) design page/upload page #3) checkout page

Target Market(s)

consumers of yard signs

Industry/Entity Type

Business

Number of Pages Required

3 page

Colors
0455a3
33a6d7
d0dfed

Requirements
Must have
• Element for user to upload their own design
• Element for users select a template -preferably sorted by industry
• Element for user to modify selected template for example - (https://www.quimbelorap.com/EditTool.aspx?T=9A1736281F03928475610B2C3D4E5F6A7B8C9D0E1F2A3B3C&S=2&M=1&CID=8827)
Nice to have
• minimal clicks to move forward with sign project

```html
<!DOCTYPE html>
<html lang="en">
<head>
<meta charset="utf-8">
<title>Stakeline — Yard Signs</title>
<link href="https://fonts.googleapis.com/css2?family=Open+Sans:wght@400;600;700&family=Raleway:wght@500;600;700&display=swap" rel="stylesheet">
<style>
:root{
  --blue:#0455a3;
  --blue-mid:#0b62b4;
  --sky:#33a6d7;
  --pale:#d0dfed;
  --navy:#0c3b69;
  --navy-dark:#0a2f55;
  --menu:#1f2633;
  --ink:#1a1a1a;
  --text:#555;
  --grey-bg:#efefef;
  --line:#cfcfcf;
}
*{box-sizing:border-box;margin:0;padding:0}
html,body{width:1200px;height:2308px;overflow:hidden}
body{position:relative;font-family:"Open Sans",Arial,sans-serif;color:var(--ink);background:#fff}
.abs{position:absolute}

/* utility bar */
.utility{top:0;left:0;width:1200px;height:37px;background:#ececec;display:flex;justify-content:flex-end;align-items:center;gap:22px;padding-right:60px;font-size:13px;color:#333}
.utility span{display:flex;align-items:center;gap:5px}
.flag{width:16px;height:11px;background:var(--blue);display:inline-block}

/* header */
.header{top:37px;left:0;width:1200px;height:112px;background:#fff}
.brand{position:absolute;left:62px;top:36px;display:flex;align-items:center;gap:10px;font-family:"Raleway",sans-serif;font-weight:600;font-size:34px;color:var(--blue)}
.brand-mark{width:30px;height:30px;background:var(--blue)}
.nav{position:absolute;left:307px;top:50px;display:flex;gap:31px;font-size:14px;color:#111}
.nav .active{color:var(--blue)}

/* blue bar */
.bar{top:149px;left:0;width:1200px;height:59px;background:var(--blue)}
.cat-toggle{position:absolute;left:62px;top:0;width:207px;height:59px;background:var(--menu);color:#fff;font-family:"Raleway",sans-serif;font-weight:700;font-size:17px;display:flex;align-items:center;gap:14px;padding-left:18px}
.burger{width:20px;height:14px;border-top:2px solid #fff;border-bottom:2px solid #fff;position:relative}
.burger::after{content:"";position:absolute;left:0;right:0;top:4px;border-top:2px solid #fff}
.search{position:absolute;left:355px;top:10px;width:507px;height:40px;display:flex}
.search input{flex:1;border:0;padding:0 14px;font-size:13px;color:#999;font-family:inherit}
.search button{width:62px;border:0;background:#222;display:flex;align-items:center;justify-content:center}
.cart{position:absolute;left:897px;top:0;height:59px;display:flex;align-items:center;gap:14px;color:#fff;font-size:15px}

/* hero */
.hero{top:208px;left:0;width:1200px;height:487px;background:linear-gradient(120deg,#dfe6ea 0%,#c9d3d9 35%,#b7aca4 60%,#3d3f44 100%)}
.cat-list{position:absolute;left:62px;top:0;width:207px;background:var(--menu);list-style:none;padding-bottom:6px}
.cat-list li{height:30.5px;line-height:30px;padding-left:22px;font-size:13px;color:#fff;border-bottom:1px solid #39414e;position:relative}
.cat-list li::before{content:"";position:absolute;left:10px;top:13px;border-left:4px solid var(--sky);border-top:3px solid transparent;border-bottom:3px solid transparent}

/* configurator */
.config{top:695px;left:0;width:1200px;height:326px;background:linear-gradient(#f7f7f7,#e9e9e9)}
.label{position:absolute;font-size:17px;color:#222}
.select{position:absolute;height:34px;background:#fff;border:1px solid var(--line);font-size:12px;color:#888;padding-left:10px;line-height:32px}
.select::after{content:"";position:absolute;right:10px;top:14px;border-top:6px solid #222;border-left:5px solid transparent;border-right:5px solid transparent}
.field{position:absolute;height:34px;background:#fff;border:1px solid var(--line);font-size:12px;color:#999;padding-left:10px;line-height:32px}
.dim{position:absolute;width:30px;height:34px;background:var(--blue);color:#fff;font-weight:700;font-size:14px;text-align:center;line-height:34px}
.panel{position:absolute;height:63px;background:#fff;border:1px solid var(--line)}
.panel-head{height:27px;background:#444;color:#fff;font-size:13px;font-weight:700;padding-left:9px;line-height:27px}
.panel-opts{display:flex;gap:30px;padding:7px 10px;font-size:12px;color:#888}
.panel-opts span{display:flex;align-items:center;gap:6px}
.radio{width:10px;height:10px;border:1px solid #bbb;border-radius:50%;background:#eee}
.radio.on{background:#666;box-shadow:inset 0 0 0 2px #fff}
.browse{position:absolute;left:997px;top:166px;width:75px;height:36px;background:#333;color:#fff;font-weight:700;font-size:14px;text-align:center;line-height:36px}
.cta{position:absolute;top:292px;width:277px;height:62px;border-radius:3px;color:#fff;font-family:"Raleway",sans-serif;font-weight:700;font-size:24px;text-align:center;line-height:62px}
.cta-start{left:341px;background:var(--blue-mid)}
.cta-upload{left:661px;background:var(--navy)}

/* intro */
.intro{top:1118px;left:0;width:1200px;text-align:center}
.intro h1{font-family:"Raleway",sans-serif;font-weight:600;font-size:32px;color:#111;margin-bottom:30px}
.intro p{width:1040px;margin:0 auto 22px;font-size:15.5px;line-height:23px;color:var(--text)}

/* featured */
.featured-title{top:1388px;left:0;width:1200px;text-align:center;font-family:"Raleway",sans-serif;font-weight:600;font-size:31px;color:#111}
.featured-rule{top:1448px;left:123px;width:1010px;height:1px;background:#ddd}
.featured-rule-accent{top:1446px;left:463px;width:286px;height:3px;background:var(--blue)}
.card{position:absolute;width:235px;height:180px;overflow:hidden}
.card-img{width:100%;height:100%}
.card-cap{position:absolute;left:0;bottom:0;width:100%;height:46px;background:rgba(90,90,90,.82);color:#fff;font-size:24px;text-align:center;line-height:46px}
.card-cap.active{background:var(--blue-mid)}
.img-banner{background:linear-gradient(135deg,#8c8f96,#b9564a 45%,#6f7682)}
.img-alu{background:linear-gradient(180deg,#2a2a2a 0 12%,#d9dcde 12%,#aeb3b6)}
.img-yard{background:linear-gradient(180deg,#a9c0cf 0,#7e9a74 40%,#5f8a3e)}
.img-rigid{background:linear-gradient(135deg,#3b3b3b,#8aa05a 50%,#c8c8c8)}

/* footer */
.footer{top:2038px;left:0;width:1200px;height:270px;background:var(--navy)}
.fcol{position:absolute;top:38px;color:#fff}
.fcol h4{font-size:14px;font-weight:700;margin-bottom:12px}
.fcol li{list-style:none;font-size:12.5px;line-height:24px}
.fcol li::before{content:"» ";}
.newsletter input{width:202px;height:34px;border:0;background:#ddd;padding-left:10px;font-size:12px;font-family:inherit;color:#444}
.newsletter button{display:block;margin-top:13px;width:92px;height:35px;border:0;background:var(--blue-mid);color:#fff;font-weight:700;font-size:14px;font-family:inherit}
.fdivider{position:absolute;top:188px;left:114px;width:985px;height:1px;background:#3d6690}
.perks{position:absolute;top:210px;left:105px;display:flex;gap:26px;color:#fff;font-size:12px;font-weight:700;line-height:17px}
.perk{display:flex;align-items:center;gap:10px}
.copyright{position:absolute;top:229px;right:68px;color:#fff;font-size:12px}
</style>
</head>
<body>

<div class="abs utility">
  <span><svg width="9" height="11" viewBox="0 0 9 11"><rect x="0" y="5" width="9" height="6" fill="#222"/><path d="M2 5V3a2.5 2.5 0 0 1 5 0v2" fill="none" stroke="#222" stroke-width="1.4"/></svg>Login</span>
  <span><svg width="10" height="11" viewBox="0 0 10 11"><circle cx="5" cy="3" r="2.6" fill="#222"/><path d="M0 11a5 5 0 0 1 10 0z" fill="#222"/></svg>My Account</span>
  <span><svg width="11" height="11" viewBox="0 0 11 11"><rect x="0" y="2" width="9" height="9" fill="none" stroke="#222" stroke-width="1.4"/><path d="M5 6 11 0M7 0h4v4" fill="none" stroke="#222" stroke-width="1.4"/></svg>Checkout ⌄</span>
  <span><i class="flag"></i>English ⌄</span>
  <span>USD ⌄</span>
</div>

<header class="abs header">
  <div class="brand"><i class="brand-mark"></i>Stakeline</div>
  <nav class="nav">
    <span class="active">BANNERS</span><span>ALUMINUM</span><span>YARD SIGNS</span><span>RIGID PLASTIC</span><span>ACRYLIC</span><span>FOAM BOARD</span><span>WINDOW DECALS</span><span>MORE ⌄</span>
  </nav>
</header>

<div class="abs bar">
  <div class="cat-toggle"><i class="burger"></i>All Catogories</div>
  <div class="search">
    <input type="text" value="Search Products....">
    <button aria-label="Search"><svg width="24" height="24" viewBox="0 0 24 24"><circle cx="10" cy="10" r="7" fill="none" stroke="#fff" stroke-width="2.6"/><path d="M15 15l7 7" stroke="#fff" stroke-width="2.8"/></svg></button>
  </div>
  <div class="cart">
    <svg width="24" height="22" viewBox="0 0 24 22"><path d="M0 2h4l3 12h13l3-9H6" fill="none" stroke="#fff" stroke-width="2.2"/><circle cx="9" cy="19" r="2" fill="#fff"/><circle cx="19" cy="19" r="2" fill="#fff"/></svg>
    <span>$0.00</span><span>0 items</span>
  </div>
</div>

<section class="abs hero" role="img" aria-label="Hand writing on a printed sign proof with a blue pen">
  <ul class="cat-list">
    <li>Banners</li><li>Aluminum Signs</li><li>Yard Signs</li><li>Rigid Plastic</li><li>Acrylic Signs</li><li>Foam Board</li><li>Opaque Window Decal</li><li>Perforated Window Decal</li><li>Frosted Window Decal</li><li>Magnets</li><li>Brushed Aluminum</li><li>Wall Decals</li>
  </ul>
</section>

<section class="abs config">
  <div class="label" style="left:91px;top:38px">Choose Sign:</div>
  <div class="select" style="left:91px;top:69px;width:227px">Banner</div>
  <div class="label" style="left:369px;top:38px">Type:</div>
  <div class="select" style="left:369px;top:69px;width:228px">Polotices</div>
  <div class="label" style="left:648px;top:38px">Size (inches):</div>
  <div class="dim" style="left:648px;top:69px">W</div>
  <div class="field" style="left:678px;top:69px;width:34px">72</div>
  <div class="dim" style="left:726px;top:69px">H</div>
  <div class="field" style="left:756px;top:69px;width:35px">45</div>
  <div class="label" style="left:843px;top:38px">Qty:</div>
  <div class="field" style="left:843px;top:69px;width:95px">1</div>
  <div class="label" style="left:966px;top:38px">Price:</div>
  <div class="field" style="left:966px;top:69px;width:103px">$145</div>

  <div class="label" style="left:91px;top:132px">Select Product Details</div>
  <div class="panel" style="left:91px;top:165px;width:226px">
    <div class="panel-head">Number of Slides</div>
    <div class="panel-opts"><span><i class="radio on"></i>1 Side</span><span><i class="radio"></i>2 Sides</span></div>
  </div>
  <div class="label" style="left:369px;top:132px">Select Product Details</div>
  <div class="panel" style="left:369px;top:165px;width:431px">
    <div class="panel-head">Number of Colors</div>
    <div class="panel-opts"><span><i class="radio on"></i>1 Color</span><span><i class="radio"></i>2 Color</span><span><i class="radio"></i>3 Color</span><span><i class="radio"></i>Full Color</span></div>
  </div>
  <div class="label" style="left:840px;top:132px">Choose Design:</div>
  <svg class="abs" style="left:983px;top:118px" width="92" height="34" viewBox="0 0 92 34"><path d="M88 32C78 10 40 2 6 12" fill="none" stroke="var(--blue-mid)" stroke-width="2.2"/><path d="M14 4 5 12l10 6" fill="none" stroke="var(--blue-mid)" stroke-width="2.2"/></svg>
  <div class="field" style="left:843px;top:166px;width:154px;height:36px"></div>
  <div class="browse">Browse</div>

  <div class="cta cta-start">Start Now !</div>
  <div class="cta cta-upload">Upload</div>
</section>

<section class="abs intro">
  <h1>We manufacture a variety of products including yard signs</h1>
  <p>Our most popular 18"x24" size can be an effective advertising solution for contractors, realty companies, lawn care services, landscapers, and other service providers and small businesses. They also work beautifully for personal use such as holiday greetings, new baby announcements, or just about any message you wish to share.</p>
  <p>The light weight of our yard signs makes them easy to move around and place almost instantly, and they are well suited to most weather conditions. The actual sign panel can be changed quickly and is so affordable that it often makes.</p>
</section>

<h2 class="abs featured-title">Featured Products</h2>
<div class="abs featured-rule"></div>
<div class="abs featured-rule-accent"></div>

<div class="card" style="left:82px;top:1515px"><div class="card-img img-banner" role="img" aria-label="People holding protest banners on a street"></div><div class="card-cap active">Banner</div></div>
<div class="card" style="left:349px;top:1515px"><div class="card-img img-alu" role="img" aria-label="Brushed aluminum company sign on a wall"></div><div class="card-cap">Aluminum Signs</div></div>
<div class="card" style="left:614px;top:1515px"><div class="card-img img-yard" role="img" aria-label="Printed yard sign standing on a lawn"></div><div class="card-cap">Yard Signs</div></div>
<div class="card" style="left:880px;top:1515px"><div class="card-img img-rigid" role="img" aria-label="Rigid plastic products and parts"></div><div class="card-cap">Rigid Plastic</div></div>

<div class="card" style="left:82px;top:1763px"><div class="card-img img-banner" role="img" aria-label="People holding protest banners on a street"></div><div class="card-cap">Banner</div></div>
<div class="card" style="left:349px;top:1763px"><div class="card-img img-alu" role="img" aria-label="Brushed aluminum company sign on a wall"></div><div class="card-cap">Aluminum Signs</div></div>
<div class="card" style="left:614px;top:1763px"><div class="card-img img-yard" role="img" aria-label="Printed yard sign standing on a lawn"></div><div class="card-cap">Yard Signs</div></div>
<div class="card" style="left:880px;top:1763px"><div class="card-img img-rigid" role="img" aria-label="Rigid plastic products and parts"></div><div class="card-cap">Rigid Plastic</div></div>

<footer class="abs footer">
  <div class="fcol" style="left:114px"><h4>MAIN MENU</h4><ul><li>Home</li><li>What's New?</li><li>Featured</li><li>Top sellers</li></ul></div>
  <div class="fcol" style="left:309px"><h4>EXTRAS</h4><ul><li>Specials</li><li>Brands</li><li>Reviews</li></ul></div>
  <div class="fcol" style="left:497px"><h4>INFORMATION</h4><ul><li>Privacy Policy</li><li>Contacts</li><li>Terms &amp; Conditions</li></ul></div>
  <div class="fcol" style="left:666px"><h4>YOUR ACCOUNT</h4><ul><li>Shipping &amp; Returns</li><li>Advanced Search</li><li>Create an Account</li><li>Log in</li></ul></div>
  <div class="fcol newsletter" style="left:878px"><h4>NEWSLETTER</h4><input type="text" value="Email Address"><button>Subscribe</button></div>
  <div class="fdivider"></div>
  <div class="perks">
    <div class="perk"><svg width="32" height="30" viewBox="0 0 32 30"><path d="M2 13h6v15H2zM10 13l6-11c3 0 4 2 3 5l-1 5h10c2 0 3 2 2 4l-3 10c-1 2-2 2-4 2H10z" fill="#cfd8e2"/></svg><span>SATISFACTION<br>100% GUARANTEED</span></div>
    <div class="perk"><svg width="36" height="26" viewBox="0 0 36 26"><path d="M0 3h22v16H0zM23 8h7l6 6v5H23z" fill="#cfd8e2"/><circle cx="7" cy="22" r="3.5" fill="#cfd8e2"/><circle cx="29" cy="22" r="3.5" fill="#cfd8e2"/></svg><span>FREE SHIPPING<br>ON ORDERS OVER $99</span></div>
    <div class="perk"><svg width="30" height="30" viewBox="0 0 30 30"><path d="M25 11A11 11 0 0 0 5 9M5 19a11 11 0 0 0 20 2" fill="none" stroke="#cfd8e2" stroke-width="3.4"/><path d="M2 3v9h9zM28 27v-9h-9z" fill="#cfd8e2"/></svg><span>7 DAY<br>EASY RETURN</span></div>
  </div>
  <div class="copyright">Copyright © 2015 Stakeline. All Rights Reserved</div>
</footer>

</body>
</html>
```